Design a single page Shopify store web page

We are looking to have a page designed for a single page Shopify store with 2 products. We already have a basic structure that we like, though we are open to suggestions. We are looking for somebody to provide a design/color scheme that we can then implement using Shopify's templating system. We can handle the implementation(HTML / CSS / jS) as we already have 2 web developers on the team, but have not been able to find a design we liked.

The job would consist of providing a mockup (photoshop or otherwise) and any vector graphics you choose to create for the site (we can provide product photos and other images).

You can also look at http://brickwellgoods.com.au for some of our design direction we have used so far

Target Market(s)

Young Australian Males (18 - 49)

Industry/Entity Type

Store

Number of Pages Required

1 page

Font styles to use
Serif
Sans Serif

Requirements
Must have
• Single Page Design
• E-commerce Product Purchase
• Manly (whatever interpretation of that you have)

```html
<!DOCTYPE html>
<html lang="en">
<head>
<meta charset="utf-8">
<title>Kit Crate — Underwear &amp; Socks Plans</title>
<link href="https://fonts.googleapis.com/css2?family=Bebas+Neue&family=Open+Sans:wght@400;600&family=Archivo+Black&family=Pinyon+Script&family=Reenie+Beanie&display=swap" rel="stylesheet">
<style>
  :root {
    --forest-deep: #1f3a33;
    --forest-mid: #4d6b45;
    --forest-light: #8fa872;
    --headline-green: #e4f0b8;
    --headline-yellow: #f3ef1f;
    --script-blue: #8fdcf4;
    --white: #ffffff;
    --field-dark: #0d0f10;
    --button-light: #eef0f1;
    --button-text: #45494c;
    --section-bg: #f4f6f7;
    --ink: #111111;
    --step-green: #a9c24c;
  }
  * { margin: 0; padding: 0; box-sizing: border-box; }
  html, body { width: 1200px; height: 1000px; overflow: hidden; }
  body { position: relative; background: var(--section-bg); font-family: "Open Sans", sans-serif; }

  .hero { position: absolute; left: 0; top: 0; width: 1200px; height: 735px; overflow: hidden; }
  .hero-photo {
    position: absolute; inset: 0;
    background:
      radial-gradient(ellipse 260px 420px at 960px 470px, rgba(170,140,110,0.55), transparent 70%),
      radial-gradient(ellipse 700px 300px at 600px 640px, rgba(120,150,80,0.55), transparent 70%),
      linear-gradient(115deg, var(--forest-deep) 0%, var(--forest-mid) 45%, var(--forest-light) 70%, var(--forest-deep) 100%);
  }
  .brand { position: absolute; left: 172px; top: 50px; display: flex; align-items: center; gap: 14px; }
  .brand-mark { width: 24px; height: 24px; background: var(--white); }
  .brand-name { font-family: "Bebas Neue", sans-serif; font-size: 60px; color: var(--white); letter-spacing: 2px; line-height: 1; }

  .main-nav { position: absolute; right: 224px; top: 74px; display: flex; gap: 20px; font-family: "Bebas Neue", sans-serif; font-size: 22px; color: var(--white); }

  .headline { position: absolute; left: 0; width: 1186px; top: 246px; text-align: center; font-family: "Bebas Neue", sans-serif; font-size: 82px; line-height: 66px; color: var(--headline-green); text-shadow: 0 2px 4px rgba(0,0,0,.35); }
  .tagline { position: absolute; left: 0; width: 1158px; top: 377px; text-align: center; font-family: "Archivo Black", sans-serif; font-size: 31px; color: var(--headline-yellow); letter-spacing: .5px; }
  .frequency { position: absolute; left: 0; width: 1138px; top: 404px; text-align: center; font-family: "Pinyon Script", cursive; font-size: 64px; color: var(--script-blue); text-shadow: 0 2px 3px rgba(0,0,0,.5); }

  .gift-note { position: absolute; left: 95px; top: 392px; font-family: "Reenie Beanie", cursive; font-size: 25px; line-height: 22px; color: var(--white); }
  .how-link { position: absolute; left: 505px; top: 612px; font-family: "Reenie Beanie", cursive; font-size: 26px; color: var(--white); }
  .arrows { position: absolute; left: 0; top: 0; }

  .signup { position: absolute; left: 320px; top: 487px; width: 500px; height: 43px; display: flex; border-radius: 5px; overflow: hidden; }
  .signup-field { flex: 1; background: var(--field-dark); color: #8b8e90; font-size: 14px; padding: 12px 20px; }
  .signup-button { width: 120px; background: var(--button-light); color: var(--button-text); font-weight: 600; font-size: 16px; text-align: center; line-height: 43px; }

  .how-it-works { position: absolute; left: 0; top: 735px; width: 1200px; height: 265px; }
  .section-title { position: absolute; left: 0; width: 1200px; top: 58px; text-align: center; font-family: "Bebas Neue", sans-serif; font-size: 52px; color: var(--ink); }
  .step { position: absolute; top: 173px; width: 240px; height: 240px; border-radius: 50%; background: var(--white); box-shadow: 0 0 6px rgba(0,0,0,.12); text-align: center; padding-top: 58px; font-family: "Bebas Neue", sans-serif; font-size: 36px; line-height: 28px; color: var(--ink); }
  .step .num { color: var(--step-green); }
  .step-1 { left: 170px; } .step-2 { left: 480px; } .step-3 { left: 790px; }
</style>
</head>
<body>
  <header class="hero">
    <div class="hero-photo" role="img" aria-label="Sunlit forest clearing with a model in red swim trunks standing at the right"></div>
    <div class="brand"><span class="brand-mark"></span><span class="brand-name">KIT CRATE</span></div>
    <nav class="main-nav">
      <span>How it works</span><span>/</span><span>Plans</span><span>/</span><span>FAQ</span><span>/</span><span>About us</span>
    </nav>
    <h1 class="headline">New underwear<br>and socks</h1>
    <p class="tagline">DELIVERED TO YOUR DOOR</p>
    <p class="frequency">Every 3 or 6 Months</p>
    <p class="gift-note">Get a free gift with<br>your first pack</p>
    <svg class="arrows" width="1200" height="735" viewBox="0 0 1200 735" fill="none" stroke="#fff" stroke-width="3" stroke-linecap="round">
      <path d="M190 445 C200 480 240 505 300 508"/>
      <path d="M268 468 L305 508 L262 528"/>
      <path d="M572 545 L574 608"/>
      <path d="M558 585 L574 610 L590 585"/>
    </svg>
    <form class="signup">
      <div class="signup-field">enter your email address</div>
      <div class="signup-button">subscribe</div>
    </form>
    <p class="how-link">See how it works !</p>
  </header>

  <section class="how-it-works">
    <h2 class="section-title">How it works</h2>
    <svg class="arrows" width="1200" height="265" viewBox="0 0 1200 265" fill="none" stroke="#111" stroke-width="3" stroke-linecap="round">
      <path d="M685 222 C720 185 770 168 820 172"/>
      <path d="M795 155 L822 172 L792 190"/>
    </svg>
    <div class="step step-1"><span class="num">1.</span> Choose<br>a plan</div>
    <div class="step step-2"><span class="num">2.</span> Choose<br>how often</div>
    <div class="step step-3"><span class="num">3.</span> Get your<br>pack</div>
  </section>
</body>
</html>
```